Billboard for Local Roofing Company

The billboard we are using will be 12' tall and 24' wide. We are looking for a clean design that is not too busy, one that stands out and is easily readable. The branding colors used should match the colors in our logo. On the billboard, it should have our slogan "Where Every Shingle Thing Matters" with the word "Shingle" in the orange.
It should also have the DRK Summit Circle logo uploaded here as well.
Lastly, it should have our phone number 555-274-1938 and our website www.quelmont-roofing.example.
I have uploaded a stock image we are thinking about using in the background of the sign...this could be darkened or otherwise obscured.
- Match fonts up if possible

```html
<!DOCTYPE html>
<html lang="en">
<head>
<meta charset="utf-8">
<title>Quelmont Roofing Billboard</title>
<link rel="stylesheet" href="https://fonts.googleapis.com/css2?family=Poppins:wght@500;600;700&family=Roboto+Slab:wght@800&display=swap">
<style>
  :root {
    --backdrop: #8f8f8f;
    --ink: #000000;
    --orange: #e35a27;
    --white: #ffffff;
    --paper: #f7f7f7;
    --seal: #3a3b40;
    --phone-disc: #1a1a1a;
  }
  html, body {
    margin: 0;
    width: 1200px;
    height: 664px;
    overflow: hidden;
    background: var(--backdrop);
    font-family: "Poppins", sans-serif;
  }
  .billboard {
    position: absolute;
    left: 57px;
    top: 61px;
    width: 1086px;
    height: 542px;
    overflow: hidden;
    background: var(--ink);
  }
  .board-shapes {
    position: absolute;
    inset: 0;
  }
  .brand-name {
    position: absolute;
    left: 20px;
    top: 232px;
    width: 600px;
    margin: 0;
    text-align: center;
    white-space: nowrap;
    font-family: "Roboto Slab", serif;
    font-weight: 800;
    font-size: 58px;
    line-height: 1;
    color: var(--white);
  }
  .phone-number {
    position: absolute;
    left: 146px;
    top: 386px;
    margin: 0;
    white-space: nowrap;
    font-weight: 500;
    font-size: 61px;
    line-height: 1;
    letter-spacing: 2px;
    color: var(--white);
  }
  .website {
    position: absolute;
    left: 52px;
    top: 476px;
    width: 536px;
    margin: 0;
    text-align: center;
    white-space: nowrap;
    font-weight: 600;
    font-size: 24px;
    line-height: 1;
    color: var(--ink);
  }
  .slogan {
    position: absolute;
    left: 686px;
    top: 339px;
    width: 380px;
    margin: 0;
    text-align: center;
    white-space: nowrap;
    font-weight: 600;
    font-size: 32px;
    line-height: 42px;
    letter-spacing: -1.2px;
    color: var(--white);
  }
  .slogan .accent { color: var(--orange); }
</style>
</head>
<body>
  <main class="billboard">
    <svg class="board-shapes" width="1086" height="542" viewBox="0 0 1086 542">
      <defs>
        <linearGradient id="roofFadeLeft" x1="0" y1="0" x2="1" y2="0">
          <stop offset="0" stop-color="#000"/>
          <stop offset="0.45" stop-color="#000"/>
          <stop offset="1" stop-color="#2a2b2f"/>
        </linearGradient>
        <linearGradient id="roofRight" x1="0" y1="0" x2="1" y2="1">
          <stop offset="0" stop-color="#26272b"/>
          <stop offset="0.6" stop-color="#141416"/>
          <stop offset="1" stop-color="#0b0b0c"/>
        </linearGradient>
      </defs>

      <rect class="photo-left" x="0" y="0" width="725" height="542" fill="url(#roofFadeLeft)"
            role="img" aria-label="Darkened photo of a shingled roof with gables"/>
      <polygon class="photo-right" points="723,0 1086,0 1086,542 611,542" fill="url(#roofRight)"
               role="img" aria-label="Darkened close-up photo of asphalt roof shingles"/>

      <rect class="brand-mark" x="280" y="126" width="80" height="80" fill="var(--orange)"/>

      <polygon class="lower-band" points="0,440 630,440 612,542 0,542" fill="var(--paper)"/>
      <polygon class="divider-stripe" points="716,0 727,0 617,542 606,542" fill="var(--orange)"/>

      <polygon class="phone-band" points="51,375 605,375 591,460 35,460" fill="var(--orange)"/>
      <circle class="phone-badge" cx="104" cy="420" r="28" fill="var(--phone-disc)"/>
      <path class="phone-icon" fill="var(--white)"
            d="M93 405c2-2 4-1 5 1l4 6c1 2 0 3-1 4l-2 2c2 4 5 7 9 9l2-2c1-1 3-1 4 0l6 4c2 1 2 3 1 5l-3 3c-2 2-5 2-8 1-9-4-16-11-20-20-1-3-1-6 1-8z"/>

      <rect class="certification-seal" x="811" y="159" width="130" height="130" rx="8" fill="var(--seal)"
            role="img" aria-label="DRK Summit Circle certification badge"/>
    </svg>

    <h1 class="brand-name">Quelmont Roofing</h1>
    <p class="phone-number">555.274.1938</p>
    <p class="website">www.quelmont-roofing.example</p>
    <p class="slogan">Where Every <span class="accent">Shingle</span><br>Thing Matters</p>
  </main>
</body>
</html>
```